Design Emoji directory website with a modern look

Please design the Emoji directory website to display a nice search box as well as design a nice search suggestion dropdown page. Example when you type keyword in Quorvex.
You can use Emojis in SVG file https://www.filebarrow.com/s/7kq2m9x4pLwz8tr/svg.rar?dl=0 to create designs.
The following are 7 example pages but please make sure the design is UNIQUE.
Main page example
https://glyphpond.info/
Content page example
https://glyphpond.info/smiling-face-with-smiling-eyes/
Category page example
https://glyphpond.info/smileys-and-emotion-category/
Holiday page example
https://glyphpond.info/holidays/
Static pages example
https://glyphpond.info/privacy-policy/
404 page not found example
https://glyphpond.info/category/
Search page example
https://glyphpond.info/?s=exchange+rate
Target Market(s)
web design
Industry/Entity Type
Website
Number of Pages Required
5+ page
Font styles to use
Other font styles liked:
- COMIC NEUE
Colors
Designer to choose colors to be used in the design.
Requirements
Must have
- Please make sure its unique, modern look, clean.
Should not have
- Do not use heavy graphics, we only use CSS style rules and SVG's emojis to make sure the site loads fast.

```html
<!DOCTYPE html>
<html lang="en">
<head>
<meta charset="utf-8">
<title>Emoji Directory – Search Results</title>
<link href="https://fonts.googleapis.com/css2?family=Arimo:wght@400;700&family=Comic+Neue:wght@400;700&display=swap" rel="stylesheet">
<style>
  :root {
    --pink: #ef7fa1;
    --pink-deep: #d6466f;
    --pink-dark: #c02d5c;
    --pink-soft: #f59bb7;
    --peach: #f3a06a;
    --accent: #d94a72;
    --ink: #1b1b1b;
    --text: #4a4a4a;
    --muted: #5c5c5c;
    --line: #e4e4e4;
    --white: #ffffff;
    --foot-link: #f38db0;
  }
  * { box-sizing: border-box; margin: 0; padding: 0; }
  html, body { width: 924px; height: 1200px; overflow: hidden; background: var(--white); }
  body { position: relative; font-family: "Arimo", Arial, sans-serif; color: var(--text); }

  .hero {
    position: absolute; left: 0; top: 0; width: 924px; height: 130px;
    background: linear-gradient(100deg, var(--peach) 0%, var(--pink) 22%, var(--pink-soft) 50%, var(--pink) 75%, var(--peach) 100%);
  }
  .brand { position: absolute; left: 159px; top: 25px; font-family: "Comic Neue", cursive; font-size: 17px; color: var(--white); letter-spacing: 1px; }
  .main-nav { position: absolute; top: 26px; left: 0; }
  .main-nav a { position: absolute; white-space: nowrap; color: var(--white); font-weight: 700; font-size: 13px; text-decoration: none; }
  .main-nav .active::after { content: ""; position: absolute; left: 4px; top: 24px; width: 29px; height: 2px; background: var(--white); border-radius: 1px; }

  .search {
    position: absolute; display: flex; align-items: center; background: var(--white); border-radius: 4px;
  }
  .search .icon { width: 18px; height: 18px; border-radius: 50%; background: var(--accent); display: flex; align-items: center; justify-content: center; flex: none; }
  .search span { font-size: 13px; color: #3a3a3a; }
  .search-hero { left: 248px; top: 77px; width: 428px; height: 32px; padding-left: 16px; gap: 12px; }
  .search-page { left: 159px; top: 219px; width: 592px; height: 34px; padding-left: 18px; gap: 12px; border: 1px solid var(--line); box-shadow: 0 1px 3px rgba(0,0,0,.08); }

  .category-bar { position: absolute; left: 0; top: 130px; width: 924px; height: 61px; background: var(--white); box-shadow: 0 2px 3px rgba(0,0,0,.08); }
  .category-bar .arrow { position: absolute; top: 23px; }
  .category { position: absolute; top: 11px; width: 70px; margin-left: -35px; text-align: center; font-size: 10px; color: #3d3d3d; }
  .category i { display: block; width: 22px; height: 22px; margin: 0 auto 8px; border-radius: 50%; }

  .results-title { position: absolute; left: 151px; top: 274px; font-family: "Comic Neue", cursive; font-size: 20px; color: var(--ink); letter-spacing: .3px; }

  .result {
    position: absolute; left: 159px; width: 592px; height: 95px; background: var(--white);
    border: 1px solid var(--line); border-radius: 7px; box-shadow: 0 1px 3px rgba(0,0,0,.07);
  }
  .result .thumb { position: absolute; left: 32px; top: 27px; width: 40px; height: 40px; border-radius: 6px; }
  .result h2 { position: absolute; left: 85px; top: 20px; font-family: "Comic Neue", cursive; font-weight: 700; font-size: 11.5px; color: var(--ink); letter-spacing: .6px; }
  .result p { position: absolute; left: 85px; top: 39px; width: 470px; font-size: 10px; line-height: 15px; color: var(--muted); letter-spacing: -.1px; }

  .site-footer { position: absolute; left: 0; top: 1039px; width: 924px; height: 161px; background: var(--pink-deep); border-radius: 16px 16px 0 0; text-align: center; color: var(--white); }
  .site-footer .foot-brand { position: absolute; left: 0; right: 0; top: 30px; font-weight: 700; font-size: 18px; }
  .site-footer .tagline { position: absolute; left: 0; right: 0; top: 58px; font-size: 9.5px; letter-spacing: -.2px; }
  .social { position: absolute; left: 0; right: 0; top: 88px; display: flex; justify-content: center; gap: 14px; }
  .social a { display: flex; align-items: center; gap: 4px; color: var(--white); font-size: 9.5px; text-decoration: none; }
  .social a::before { content: ""; width: 9px; height: 9px; border: 1px solid var(--white); border-radius: 50%; }
  .copyright { position: absolute; left: 0; bottom: 0; width: 924px; height: 33px; background: var(--pink-dark); color: var(--foot-link); font-size: 9.5px; line-height: 33px; letter-spacing: -.2px; }
</style>
</head>
<body>

<header class="hero" role="img" aria-label="Pink banner with large smiling emoji faces and hearts">
  <div class="brand">LOGO</div>
  <nav class="main-nav">
    <a class="active" href="#" style="left:475px">People</a>
    <a href="#" style="left:533px">Emoticon</a>
    <a href="#" style="left:607px">Nature</a>
    <a href="#" style="left:664px">Animals</a>
    <a href="#" style="left:730px">Life</a>
  </nav>
  <div class="search search-hero">
    <div class="icon"><svg width="8" height="8" viewBox="0 0 10 10"><circle cx="4" cy="4" r="3" fill="none" stroke="#fff" stroke-width="1.6"/><line x1="6.2" y1="6.2" x2="9" y2="9" stroke="#fff" stroke-width="1.8" stroke-linecap="round"/></svg></div>
    <span>Painter Face</span>
  </div>
</header>

<nav class="category-bar">
  <svg class="arrow" style="left:158px" width="8" height="12" viewBox="0 0 8 12"><polyline points="6,1 1.5,6 6,11" fill="none" stroke="#555" stroke-width="1.1"/></svg>
  <div class="category" style="left:202px"><i role="img" aria-label="Guitar emoji" style="background:#d3334a"></i>Music</div>
  <div class="category" style="left:271px"><i role="img" aria-label="Face with medical mask emoji" style="background:#ffcc4d"></i>Health</div>
  <div class="category" style="left:336px"><i role="img" aria-label="United States flag emoji" style="background:#3b5fa8;border-radius:3px;height:18px;margin-top:2px;margin-bottom:10px"></i>Flags</div>
  <div class="category" style="left:412px"><i role="img" aria-label="Moai statue emoji" style="background:#99aab5;border-radius:6px"></i>Monuments</div>
  <div class="category" style="left:489px"><i role="img" aria-label="Tangerine emoji" style="background:#f4900c"></i>Fruits</div>
  <div class="category" style="left:558px"><i role="img" aria-label="Snowman emoji" style="background:#dfe6ec"></i>Seasons</div>
  <div class="category" style="left:635px"><i role="img" aria-label="Person with veil emoji" style="background:#c98a6b"></i>Wedding</div>
  <div class="category" style="left:705px"><i role="img" aria-label="Pilot emoji" style="background:#3b3f44"></i>Work</div>
  <svg class="arrow" style="left:744px" width="8" height="12" viewBox="0 0 8 12"><polyline points="2,1 6.5,6 2,11" fill="none" stroke="#555" stroke-width="1.1"/></svg>
</nav>

<main>
  <div class="search search-page">
    <div class="icon"><svg width="8" height="8" viewBox="0 0 10 10"><circle cx="4" cy="4" r="3" fill="none" stroke="#fff" stroke-width="1.6"/><line x1="6.2" y1="6.2" x2="9" y2="9" stroke="#fff" stroke-width="1.8" stroke-linecap="round"/></svg></div>
    <span>Painter Face</span>
  </div>

  <h1 class="results-title">Search Results for: exchange rate</h1>

  <article class="result" style="top:326px">
    <div class="thumb" role="img" aria-label="Currency exchange emoji" style="background:#66757f"></div>
    <h2>Currency Exchange Emoji</h2>
    <p>Lorem ipsum dolor sit amet, consectetur adipiscing elit, sed do eiusmod tempor incididunt ut labore et dolore magna aliqua. Ut enim ad minim veniam, quis nostrud exercitation ullamco laboris nisi ut aliquip ex ea</p>
  </article>
  <article class="result" style="top:440px">
    <div class="thumb" role="img" aria-label="Dollar banknote emoji" style="background:#5c913b;height:34px;top:30px"></div>
    <h2>Currency Exchange Emoji</h2>
    <p>Lorem ipsum dolor sit amet, consectetur adipiscing elit, sed do eiusmod tempor incididunt ut labore et dolore magna aliqua. Ut enim ad minim veniam, quis nostrud exercitation ullamco laboris nisi ut aliquip ex ea</p>
  </article>
  <article class="result" style="top:553px">
    <div class="thumb" role="img" aria-label="Euro banknote emoji" style="background:#3b88c3;height:34px;top:32px"></div>
    <h2>Currency Exchange Emoji</h2>
    <p>Lorem ipsum dolor sit amet, consectetur adipiscing elit, sed do eiusmod tempor incididunt ut labore et dolore magna aliqua. Ut enim ad minim veniam, quis nostrud exercitation ullamco laboris nisi ut aliquip ex ea</p>
  </article>
  <article class="result" style="top:666px">
    <div class="thumb" role="img" aria-label="Credit card emoji" style="background:#ffac33;height:30px;top:32px"></div>
    <h2>Currency Exchange Emoji</h2>
    <p>Lorem ipsum dolor sit amet, consectetur adipiscing elit, sed do eiusmod tempor incididunt ut labore et dolore magna aliqua. Ut enim ad minim veniam, quis nostrud exercitation ullamco laboris nisi ut aliquip ex ea</p>
  </article>
  <article class="result" style="top:780px">
    <div class="thumb" role="img" aria-label="Chart with upwards trend and yen sign emoji" style="background:#77b255"></div>
    <h2>Currency Exchange Emoji</h2>
    <p>Lorem ipsum dolor sit amet, consectetur adipiscing elit, sed do eiusmod tempor incididunt ut labore et dolore magna aliqua. Ut enim ad minim veniam, quis nostrud exercitation ullamco laboris nisi ut aliquip ex ea</p>
  </article>
  <article class="result" style="top:894px">
    <div class="thumb" role="img" aria-label="Money bag emoji" style="background:#fdd888;border-radius:50% 50% 45% 45%;width:36px;left:34px"></div>
    <h2>Currency Exchange Emoji</h2>
    <p>Lorem ipsum dolor sit amet, consectetur adipiscing elit, sed do eiusmod tempor incididunt ut labore et dolore magna aliqua. Ut enim ad minim veniam, quis nostrud exercitation ullamco laboris nisi ut aliquip ex ea</p>
  </article>
</main>

<footer class="site-footer">
  <div class="foot-brand">LOGO</div>
  <p class="tagline">Lorem Ipsum is simply dummy text of the printing and typesetting industry.</p>
  <div class="social">
    <a href="#">Hubbo</a>
    <a href="#">Kivvi</a>
    <a href="#">Lumo</a>
  </div>
  <div class="copyright">Copyright © Emoji Directory | All Rights Deserved | Privacy Policy | Contact Us</div>
</footer>

</body>
</html>
```